Need a book cover for a "Get a Job" book for law students.

I wrote a simple, practical book for the law students who are in the BOTTOM of the class, those with low grade-point averages (GPAs) or from low-ranked law schools. It's a tough job market and it's hard for them to find jobs because there's a lot of competition for the few jobs, and with low GPAs good firms don't want to hire these students.
This 75-page book shows them how to use personal-branding and marketing techniques to still get a good job after they graduate. The tone of the design should be REALISTIC BUT HOPEFUL.
They thought they'd rank at the top of the class but instead they're devastated to find they're near the bottom. Now they have $150,000 in student debt and might end up working at Brewhaven.

Target Market(s)

The target audience is 30 years old, smart, hard working, and SCARED.

Industry/Entity Type

Legal

Font styles to use
Serif
Sans Serif

Colors
3176b5
0455a3
cedeed
85acd3
eaf1f7

Requirements
Must have
• We need a big bold HEADLINE that will be readable at a small Novarix thumbnail size.
• BOOK TITLE:
• The Complete Law Graduate Hire-Me Roadmap.
• Smaller sub-head:
• A step-by-step guide to help students in the bottom 75% land a great job.
• Large:
• By Dale Penwick, JD
• Smaller:
• Edited by Maribeth Quill, Esq.
• Include this call-out blurb on the cover:
• "Every law student who wants a great job should read this book!" -Lora Venton, Venton & Harlow.
• The BACK cover should have roughed-in fake text, and a small "About the Author" biographical section with my face on it (photo attached). The bio text can be faked too; I'm just looking for design.
Nice to have
• I want a single strong graphic IMAGE that grabs their attention, looks professional, and conveys the stress that they're feeling, but shows them that they'll be successful if they buy this book.
• The attached photos of abused books represent their current emotions, but we might instead want something more POSITIVE and uplifting, if you can come up with something. What represents their future success?
Should not have
• We're trying to AVOID the obvious "Law" cliches like gavels, columns, handshakes, buildings, skylines, courthouses, etc. UNLESS you can find a way to use them in a creative way. Do not use them in a literal way, e.g. use a gavel to represent Law. That's too obvious and boring. But for example, if it's broken, that's more unique and potentially eye-catching.

```html
<!DOCTYPE html>
<html lang="en">
<head>
<meta charset="utf-8">
<title>The Complete Law Graduate Hire-Me Roadmap — Book Cover</title>
<link href="https://fonts.googleapis.com/css2?family=Oswald:wght@400;500;600&display=swap" rel="stylesheet">
<style>
  :root {
    --bg-edge: #07080f;
    --bg-core: #161a31;
    --rule-purple: #3a2652;
    --stripe-gold: #a68e1f;
    --text-white: #ffffff;
    --text-gold: #a38c1c;
    --text-plum: #3b2653;
    --burst-light: #d6c845;
    --burst-mid: #7f7420;
  }
  html, body {
    margin: 0;
    padding: 0;
    width: 768px;
    height: 1200px;
    overflow: hidden;
    background: var(--bg-edge);
  }
  .cover {
    display: block;
    width: 768px;
    height: 1200px;
    font-family: "Oswald", "Arial Narrow", sans-serif;
  }
  .blurb { fill: var(--text-plum); font-size: 21px; font-weight: 400; }
  .title-line { fill: var(--text-white); font-weight: 400; }
  .title-hero { fill: var(--text-white); font-weight: 500; }
  .rule { fill: var(--rule-purple); }
  .stripe { fill: var(--stripe-gold); }
  .subtitle { fill: var(--text-gold); font-size: 35px; font-weight: 500; }
  .author { fill: var(--text-white); font-size: 72px; font-weight: 500; }
  .editor { fill: var(--text-plum); font-size: 29px; font-weight: 500; }
</style>
</head>
<body>
<svg class="cover" viewBox="0 0 768 1200" xmlns="http://www.w3.org/2000/svg">
  <defs>
    <radialGradient id="bg-glow" cx="50%" cy="45%" r="65%">
      <stop offset="0%" stop-color="var(--bg-core)"/>
      <stop offset="100%" stop-color="var(--bg-edge)"/>
    </radialGradient>
    <radialGradient id="burst-fill" cx="50%" cy="48%" r="50%">
      <stop offset="0%" stop-color="var(--burst-light)" stop-opacity="0.55"/>
      <stop offset="55%" stop-color="var(--burst-mid)" stop-opacity="0.45"/>
      <stop offset="100%" stop-color="var(--burst-mid)" stop-opacity="0"/>
    </radialGradient>
  </defs>

  <rect class="background" width="768" height="1200" fill="url(#bg-glow)"/>

  <ellipse class="check-burst" role="img" aria-label="Field of distressed gold check marks radiating behind the title"
           cx="400" cy="540" rx="340" ry="400" fill="url(#burst-fill)"/>

  <g class="blurb-group">
    <text class="blurb" x="696" y="74" text-anchor="end" textLength="622" lengthAdjust="spacingAndGlyphs">“EVERY LAW STUDENT WHO WANTS A GREAT JOB SHOULD READ THIS BOOK”</text>
    <text class="blurb" x="696" y="101" text-anchor="end">-LORA VENTON, VENTON &amp; HARLOW</text>
  </g>

  <g class="title-block">
    <rect class="rule" x="54" y="316" width="656" height="8"/>

    <text class="title-line" x="58" y="388" font-size="68" textLength="426" lengthAdjust="spacingAndGlyphs">THE COMPLETE</text>
    <g class="stripes stripes-top">
      <rect class="stripe" x="496" y="336" width="214" height="7"/>
      <rect class="stripe" x="496" y="352" width="214" height="7"/>
      <rect class="stripe" x="496" y="368" width="214" height="7"/>
      <rect class="stripe" x="496" y="384" width="214" height="7"/>
    </g>

    <text class="title-line" x="58" y="484" font-size="100" textLength="652" lengthAdjust="spacingAndGlyphs">LAW GRADUATE</text>

    <text class="title-hero" x="58" y="600" font-size="128" textLength="652" lengthAdjust="spacing">HIRE-ME</text>

    <g class="stripes stripes-bottom">
      <rect class="stripe" x="54" y="626" width="302" height="7"/>
      <rect class="stripe" x="54" y="642" width="302" height="7"/>
      <rect class="stripe" x="54" y="658" width="302" height="7"/>
      <rect class="stripe" x="54" y="674" width="302" height="7"/>
    </g>
    <text class="title-line" x="368" y="680" font-size="68" textLength="340" lengthAdjust="spacingAndGlyphs">ROADMAP</text>

    <rect class="rule" x="54" y="692" width="656" height="8"/>
  </g>

  <g class="subtitle-group">
    <text class="subtitle" x="384" y="969" text-anchor="middle" textLength="644" lengthAdjust="spacingAndGlyphs">A STEP-BY-STEP GUIDE TO HELP STUDENTS</text>
    <text class="subtitle" x="384" y="1017" text-anchor="middle" textLength="597" lengthAdjust="spacingAndGlyphs">IN THE BOTTOM 75% LAND A GREAT JOB</text>
  </g>

  <text class="author" x="384" y="1096" text-anchor="middle" textLength="584" lengthAdjust="spacingAndGlyphs">DALE PENWICK, JD</text>
  <text class="editor" x="384" y="1138" text-anchor="middle" textLength="392" lengthAdjust="spacingAndGlyphs">EDITED BY MARIBETH QUILL, ESQ</text>
</svg>
</body>
</html>
```